Plakat-Design für einen Pflegedienst
Zielgruppe
Unter Pflegedienst besteht jetzt seit 10 Jahren, Dazu würden wir gerne ein Werbeplakat an verschiedenen Standpunkten veröffentlichen. Draus sollte hervorgehen, dass wir 10 Jahre bestehen Bilder sollten aus den Portalen verwendet werden. Der Slogan könnte vielleicht lauten:
Seit 10 Jahren rund um die Uhr für Sie im Einsatz.
oder gerne auch eine andere Idee für den Slogan.
Die Plakate sollen bei 468 Aushang veröffentlicht werden. Da wir zwei Filialen betrieben, müssten zwei verschiedene Varianten mit zwei Logos und Telefonnummern erstellt werden.
Aufgabenstellung
Das Plakat sollte modern und elegant sein.

```html
<!DOCTYPE html>
<html lang="de">
<head>
<meta charset="utf-8">
<title>Plakat Pflegedienst – Seit 10 Jahren</title>
<link rel="stylesheet" href="https://fonts.googleapis.com/css2?family=Bebas+Neue&family=Lato:wght@700;900&display=swap">
<style>
  :root {
    --page-bg: #ffffff;
    --sun-yellow: #f3d24a;
    --sun-yellow-light: #f5df72;
    --scrub-teal: #2fa9aa;
    --band-teal: #6bc1c9;
    --ink-teal: #1ba3b3;
    --label-white: #f7f7f5;
    --logo-black: #151515;
  }
  * { box-sizing: border-box; margin: 0; padding: 0; }
  html, body {
    width: 1200px; height: 800px; overflow: hidden;
    background: var(--page-bg);
  }
  .poster {
    position: absolute;
    left: 332px; top: 20px;
    width: 536px; height: 760px;
    overflow: hidden;
    background: var(--sun-yellow);
    font-family: "Bebas Neue", "Oswald", sans-serif;
  }
  .poster__photo {
    position: absolute; left: 0; top: 0;
    width: 100%; height: 380px;
    background:
      radial-gradient(ellipse 300px 260px at 78% 100%, var(--scrub-teal) 0%, var(--scrub-teal) 45%, rgba(47,169,170,0) 100%),
      linear-gradient(100deg, var(--sun-yellow-light) 0%, var(--sun-yellow) 55%, #e9c93e 100%);
  }
  .poster__band {
    position: absolute; left: 0; top: 380px;
    width: 100%; height: 241px;
    background: var(--band-teal);
  }
  .poster__footer {
    position: absolute; left: 0; top: 621px;
    width: 100%; height: 139px;
    background: var(--sun-yellow);
  }
  .label {
    position: absolute;
    background: var(--label-white);
    color: var(--ink-teal);
    line-height: 1;
    white-space: nowrap;
    transform: translate(-50%, -50%) rotate(var(--tilt));
    padding: 0.12em 0.3em 0.02em;
  }
  .label--role     { left: 112px; top: 183px; font-size: 42px; --tilt: 33deg; }
  .label--hero     { left: 136px; top: 284px; font-size: 48px; --tilt: 25deg; }
  .label--years    { left: 170px; top: 417px; font-size: 58px; --tilt: 0deg; padding: 0.1em 0.28em 0; }
  .label--clock    { left: 287px; top: 493px; font-size: 78px; --tilt: -16deg; }
  .label--service  { left: 314px; top: 570px; font-size: 58px; --tilt: -12deg; }

  .contact {
    position: absolute;
    font-family: "Lato", Arial, sans-serif;
    font-weight: 700;
    font-size: 20px;
    line-height: 28px;
    letter-spacing: 0.12em;
    color: var(--ink-teal);
  }
  .contact--online  { left: 17px; top: 649px; }
  .contact--address { right: 20px; top: 646px; text-align: right; line-height: 30px; }
  .brand-slot {
    position: absolute;
    left: 297px; top: 694px;
    transform: translate(-50%, -50%);
    font-family: "Lato", Arial, sans-serif;
    font-weight: 900;
    font-size: 28px;
    line-height: 39px;
    letter-spacing: 0.12em;
    color: var(--logo-black);
    text-align: center;
  }
</style>
</head>
<body>
  <main class="poster">
    <div class="poster__photo" role="img" aria-label="Foto: Pflegekraft in türkiser Berufskleidung mit Mundschutz in Superheldinnen-Pose vor gelbem Hintergrund"></div>
    <div class="poster__band"></div>
    <div class="poster__footer"></div>

    <p class="label label--role">Pflegende*r</p>
    <p class="label label--hero">Superheld*in</p>
    <h1 class="label label--years">Seit 10 Jahren</h1>
    <p class="label label--clock">Rund um die Uhr</p>
    <p class="label label--service">Für Sie im Einsatz</p>

    <p class="contact contact--online">Website<br>Social Media<br>Telefonnummer</p>
    <p class="brand-slot">IHR<br>LOGO</p>
    <p class="contact contact--address">Kontakt<br>Straße<br>PLZ ORT</p>
  </main>
</body>
</html>
```